Garden Planting Plan Design Project

We sell DIY designer garden makeover kits, consisting of living plants and how-to planting plans in different styles, e.g. Tropical or Mediterranean gardens.
We need a design template for the how-to planting plan, which will then be laid out with each garden's kits content.
The winning designer will be hired to complete 6 design plans in total.
Idea sketches and concepts, rather than finished pieces, are welcome at this stage.
This document, the "Patio Petalcraft Primer", needs to embody our brand and present the information in an original, slick, contemporary and cool way.
The document will be available to customers as a download PDF, and as a printed piece (on recycled stock). For the downloadable, people will print it on their home printers, so this must be taken into consideration in the design (i.e. avoiding background colours or large photos which wont look good on low-quality printers). We dont think this will constrain you though.
The document should have 6-8 pages - we dont mind 'white space' and can see interesting possibilities for die cuts, use of the fold, and infographics.
The key is to use our great content in the most beautiful way possible. It's all about getting the customer excited about the design possibilities of their garden kit - we want them to be so delighted with the document that they put it on their "inspiration" pinboard.
If you need more direction, we will feedback asap.
Updates
Here is an example of a garden design plan which might spark your ideas.
Please note we are looking for concepts for this comp. Not expecting finished pieces. We are looking to work with a great designer who gets our brand and audience.
Re ICONS. If you are using, they should be:
? Sun,
? Part Shade
? Shade
? Garden Bed
? Pot
? Flower
Thanks all!!
Target Market(s)
Design-conscious urban professionals (male and female), decorators/DIYers, inexperienced gardeners (got to be easy to follow).
Requirements
Must have
- Content, more notes and examples of documents designs we like are in the Brief folder.
Should not have
- NO stock imagery please.

```html
<!DOCTYPE html>
<html lang="en">
<head>
<meta charset="utf-8">
<title>Patio Petalcraft Primer – Preparing and planting</title>
<link href="https://fonts.googleapis.com/css2?family=Montserrat:wght@600;700&family=Questrial&display=swap" rel="stylesheet">
<style>
  :root{
    --ink:#3a3a3a;
    --heading:#2f2f2f;
    --white:#ffffff;
    --accent:#c9d64a;
    --line:#d6d6d6;
    --clivia-a:#1d2a14; --clivia-b:#c2571d;
    --ti-a:#3a0d14; --ti-b:#8c1f3a;
    --coleus-a:#141a10; --coleus-b:#6b2a3a;
    --palm-a:#f3f4ee; --palm-b:#7f9a58;
  }
  *{box-sizing:border-box;margin:0;padding:0}
  html,body{width:839px;height:1200px;overflow:hidden;background:var(--white)}
  .page{position:relative;width:839px;height:1200px;border:1px solid var(--line);
    font-family:"Questrial",sans-serif;color:var(--ink)}
  .guide{position:absolute;left:30px;top:30px;width:388px}
  .guide h1,.guide h2{font-family:"Montserrat",sans-serif;font-weight:700;color:var(--heading);line-height:1.08}
  .guide h1{font-size:27px;margin-bottom:14px}
  .guide h2{font-size:27px;margin:26px 0 12px}
  .guide p{font-size:13.4px;line-height:1.42;margin-bottom:13px}
  .plants{position:absolute;left:432px;top:30px;width:378px}
  .plant{position:relative;height:282px;overflow:hidden}
  .plant .photo{position:absolute;inset:0}
  .plant .info{position:absolute;right:14px;width:200px;text-align:right;color:var(--white)}
  .plant h3{font-family:"Montserrat",sans-serif;font-weight:700;font-size:28px;margin-bottom:8px}
  .plant .desc{font-size:12px;line-height:1.38}
  .plant .species{position:absolute;right:14px;font-size:11.5px;color:var(--white)}
  .plant .species b{font-family:"Montserrat",sans-serif;font-weight:700;color:var(--accent)}
  .clivia .photo{background:radial-gradient(circle at 35% 45%,var(--clivia-b),var(--clivia-a) 60%)}
  .clivia .info{top:16px}
  .clivia .species{bottom:14px}
  .ti .photo{background:linear-gradient(100deg,var(--ti-b) 0%,var(--ti-a) 55%)}
  .ti .info{top:70px;width:190px}
  .ti .species{bottom:18px}
  .coleus .photo{background:linear-gradient(100deg,var(--coleus-b) 0%,var(--coleus-a) 55%)}
  .coleus .info{top:60px;width:196px}
  .coleus .species{bottom:18px}
  .palm .photo{background:linear-gradient(100deg,var(--palm-b) 0%,var(--palm-a) 50%)}
  .palm .info{top:70px;width:200px;color:var(--heading)}
  .palm .species{bottom:28px;color:var(--heading)}
  .palm .species b{color:#8aa23a}
</style>
</head>
<body>
<main class="page">
  <section class="guide">
    <h1>Preparing and planting<br>your new garden</h1>
    <p>Mark out the dimensions of your bed using stakes at each corner tied with string and run along the lines with a spade. Our gardens are designed for a 2 x 1.5m space, but the bed doesn't have to be rectangular. For an organic shape, try using a garden hose to make curves, and mark the edges with edging spray paint.</p>
    <p>Most gardens prefer rich, well-draining soil, so a slightly raised bed mixing fresh, well-fertilised soil with your natural soil is ideal. Till the bed to a 30cm depth with a hoe or spade. Mix in the fresh soil, compost and a good couple of handfuls of slow release fertiliser and water-saving crystals.</p>
    <p>For potted gardens, first brush or hose out the pots to ensure a hygienic home for your new plants. Place your pots in position – the pot design plan fits a space 2 x 1.5m. Lay a 5cm layer of gravel at the bottom of each pot for drainage, then half-fill with soil mixed with compost and fertiliser.</p>
    <p>Now place the plants in their pots in the positions detailed by the planting plan design, taking note in your spacing of how wide each plant is likely to grow. Then remove from their plastic pots, loosen the roots a little, and place the plants into the soil at the same level they were growing in the pot. Gently firm the soil around each plant with your hands, then water well. Finally lay an 8cm layer of mulch around the base of the plants.</p>
    <p>Water once a day (morning or evening) for the first month to help the plants settle in. Thereafter, watering once or twice a week should be enough for Patio Petalcraft gardens.</p>
    <p>We hope you get years of pleasure from your new garden!</p>
    <h2>Care Tips</h2>
    <p>To keep your plants super-happy, fertilise them every two weeks or so in the warmer months with a thin layer of mix of cow manure and mushroom compost worked in with a trowel (move the mulch and then re-apply after fertilising). Many flowering plants and veges also love a good drink of liquid fertiliser like seaweed tonic or worm-tea every fortnight.</p>
    <p>Tip: Put an alert on your phone calendar to remind you to water and feed.</p>
  </section>

  <section class="plants">
    <article class="plant clivia">
      <div class="photo" role="img" aria-label="Photo of orange clivia flowers against dark green foliage"></div>
      <div class="info">
        <h3>Clivia</h3>
        <p class="desc">A popular plant for shady spots as it is very hardy and the vivid orange flowers a spectacular against dark green foliage.</p>
      </div>
      <p class="species">Clivia Hybrid | <b>TALL ACCENT</b></p>
    </article>
    <article class="plant ti">
      <div class="photo" role="img" aria-label="Photo of purple and pink Ti plant leaves"></div>
      <div class="info">
        <h3>Ti Plant</h3>
        <p class="desc">Purple, hot pink-tinged leaves with white-pink flowers trade in late spring.</p>
      </div>
      <p class="species">Cordyline Fruticosa 'Rubra' | <b>ACCENT</b></p>
    </article>
    <article class="plant coleus">
      <div class="photo" role="img" aria-label="Photo of variegated coleus leaves"></div>
      <div class="info">
        <h3>Coleus</h3>
        <p class="desc">Teardrop shaped variegated leaves in fabulous colour combinations including green, pink, yellow, black maroon, and red flower stalks in late spring.</p>
      </div>
      <p class="species">Solenostemon Scutellarioides | <b>ACCENT</b></p>
    </article>
    <article class="plant palm">
      <div class="photo" role="img" aria-label="Photo of a bamboo palm with fern-like fronds"></div>
      <div class="info">
        <h3>Bamboo Palm</h3>
        <p class="desc">Graceful fern-like palm that grows to 2.5m with multiple stems like bamboo.</p>
      </div>
      <p class="species">Chamaedorea Seifrizii | <b>TALL ACCENT</b></p>
    </article>
  </section>
</main>
</body>
</html>
```